Legal Stationary

A full set of stationery is required
The image and logo, along with colour, are set and attached.
The style should be modern, clean, and corporate. Not just a basic template off the web.
In addition to the address/website/email/phone fields for DX and KWT number, with the text “the firm is authorised and regulated by the KWT”
All files in all formats will be needed to allow editing after. Initial setup of templates will be required, and details for 4 business cards will be supplied.
Target Market(s)
Consumers of legal services
Industry/Entity Type
Legal

```html
<!DOCTYPE html>
<html lang="en">
<head>
<meta charset="utf-8">
<title>HVR LAW – Stationery Set</title>
<link href="https://fonts.googleapis.com/css2?family=Poppins:wght@400;500;600&family=Montserrat:wght@600&family=Libre+Baskerville&display=swap" rel="stylesheet">
<style>
  :root {
    --brand-blue: #253c92;
    --brand-blue-light: #2c459c;
    --ink: #111111;
    --paper: #ffffff;
    --board: #cfd5d5;
    --board-edge: #bfc6c6;
  }
  * { margin: 0; padding: 0; box-sizing: border-box; }
  html, body { width: 1200px; height: 922px; overflow: hidden; }
  body {
    position: relative;
    background: radial-gradient(ellipse at 50% 40%, #d7dcdc 0%, var(--board) 60%, var(--board-edge) 100%);
    font-family: "Poppins", sans-serif;
    color: var(--ink);
  }
  .icon-defs { position: absolute; width: 0; height: 0; }

  .set-label {
    position: absolute;
    font-family: "Libre Baskerville", serif;
    font-size: 35px;
    color: #f4f6f6;
    text-shadow: 1px 1px 1px rgba(0,0,0,.18), -1px -1px 1px rgba(255,255,255,.6);
    transform: translateX(-50%);
    white-space: nowrap;
    letter-spacing: 1px;
  }

  .sheet { position: absolute; overflow: hidden; box-shadow: 0 6px 14px rgba(0,0,0,.22); }

  .brand {
    display: inline-flex; align-items: center; gap: .3em;
    font-family: "Montserrat", sans-serif; font-weight: 600;
    color: var(--brand-blue); white-space: nowrap; line-height: 1;
  }
  .brand-square { width: .72em; height: .72em; background: currentColor; display: inline-block; }
  .brand--white { color: var(--paper); }

  .contact-line { position: absolute; display: flex; align-items: center; gap: 5px; white-space: nowrap; }
  .contact-icon { fill: var(--brand-blue); flex: none; }

  .wave { position: absolute; left: 0; bottom: 0; width: 100%; z-index: 0; }
  .footer-ref { position: absolute; z-index: 1; color: var(--paper); white-space: nowrap; letter-spacing: .4px; }

  /* Letterhead */
  .letterhead { left: 111px; top: 103px; width: 497px; height: 702px; background: var(--paper); }
  .letterhead .brand { position: absolute; left: 26px; top: 33px; font-size: 32px; }
  .letterhead .contact-line { right: 34px; font-size: 10.5px; font-weight: 500; flex-direction: row-reverse; }
  .letterhead .contact-icon { width: 10px; height: 10px; }
  .letterhead .wave { height: 40px; }
  .letterhead .footer-ref { right: 14px; bottom: 7px; font-size: 10px; line-height: 12px; font-weight: 500; }

  /* Business card front */
  .card-front { left: 731px; top: 103px; width: 277px; height: 158px; background: var(--brand-blue); }
  .card-front .brand { position: absolute; left: 50%; top: 60px; transform: translateX(-50%); font-size: 32px; }
  .card-front .regulator-note { position: absolute; left: 0; right: 0; top: 140px; text-align: center; color: var(--paper); font-size: 7px; }

  /* Business card back */
  .card-back { left: 731px; top: 278px; width: 277px; height: 158px; background: var(--paper); }
  .card-back .brand { position: absolute; left: 10px; top: 12px; font-size: 22px; }
  .card-back .person { position: absolute; right: 11px; top: 8px; text-align: right; }
  .card-back .person-name { font-size: 15px; color: var(--brand-blue); line-height: 1.1; }
  .card-back .person-name b { font-weight: 600; }
  .card-back .person-role { font-size: 7.5px; font-weight: 500; }
  .card-back .accent-bar { position: absolute; right: 0; top: 9px; width: 7px; height: 25px; background: var(--brand-blue); }
  .card-back .address { position: absolute; left: 10px; top: 71px; font-size: 7.8px; line-height: 10.5px; }
  .card-back .contact-line { left: 10px; font-size: 7.8px; line-height: 9px; }
  .card-back .contact-icon { width: 7px; height: 7px; }
  .card-back .wave { height: 32px; }
  .card-back .footer-ref { right: 14px; bottom: 3px; font-size: 7px; text-align: right; line-height: 8.5px; }

  /* Envelope front */
  .envelope-front { left: 686px; top: 461px; width: 373px; height: 166px; background: var(--paper); }
  .envelope-front .brand { position: absolute; right: 10px; top: 14px; font-size: 22px; }
  .envelope-front .address { position: absolute; left: 244px; top: 67px; font-size: 8.8px; line-height: 11px; }
  .envelope-front .contact-line { left: 244px; font-size: 8.8px; line-height: 10px; }
  .envelope-front .contact-icon { width: 8px; height: 8px; }
  .envelope-front .wave { height: 28px; }
  .envelope-front .footer-ref { right: 16px; bottom: 5px; font-size: 7px; line-height: 9px; }

  /* Envelope back */
  .envelope-back { left: 687px; top: 645px; width: 372px; height: 165px; background: var(--brand-blue); }
  .envelope-back .flap {
    position: absolute; left: 4px; right: 6px; top: 0; height: 56px;
    background: var(--brand-blue-light); border-radius: 0 0 12px 12px;
    box-shadow: 0 5px 10px rgba(0,0,0,.25);
  }
  .envelope-back .brand { position: absolute; left: 50%; top: 23px; transform: translateX(-50%); font-size: 7px; }
</style>
</head>
<body>

<svg class="icon-defs" aria-hidden="true">
  <defs>
    <symbol id="icon-phone" viewBox="0 0 24 24"><path d="M6.6 10.8a15 15 0 0 0 6.6 6.6l2.2-2.2c.3-.3.7-.4 1-.2 1.1.4 2.3.6 3.6.6.6 0 1 .4 1 1V20c0 .6-.4 1-1 1A17 17 0 0 1 3 4c0-.6.4-1 1-1h3.5c.6 0 1 .4 1 1 0 1.3.2 2.5.6 3.6.1.3 0 .7-.2 1z"/></symbol>
    <symbol id="icon-globe" viewBox="0 0 24 24"><path d="M12 2a10 10 0 1 0 0 20 10 10 0 0 0 0-20zm-1 17.9A8 8 0 0 1 4.2 10L9 15v1a2 2 0 0 0 2 2zm6.9-2.5A2 2 0 0 0 16 16h-1v-3a1 1 0 0 0-1-1H8v-2h2a1 1 0 0 0 1-1V7h2a2 2 0 0 0 2-2v-.4a8 8 0 0 1 2.9 12.8z"/></symbol>
    <symbol id="icon-mail" viewBox="0 0 24 24"><path d="M3 5h18a1 1 0 0 1 1 1v12a1 1 0 0 1-1 1H3a1 1 0 0 1-1-1V6a1 1 0 0 1 1-1zm1 2.4V17h16V7.4l-8 5.2zM5.2 7 12 11.4 18.8 7z"/></symbol>
    <symbol id="icon-pin" viewBox="0 0 24 24"><path d="M12 1a7 7 0 0 0-7 7c0 5 7 12 7 12s7-7 7-12a7 7 0 0 0-7-7zm0 10a3 3 0 1 1 0-6 3 3 0 0 1 0 6zM6 21h12v2H6z"/></symbol>
    <symbol id="footer-wave" viewBox="0 0 500 40" preserveAspectRatio="none">
      <path fill="#253c92" d="M0 24 C100 40 240 38 300 28 C380 15 450 11 500 12 L500 40 L0 40Z"/>
      <path fill="#111111" d="M0 2 C80 22 170 32 260 34 C170 36 70 30 0 12Z"/>
      <path fill="#111111" d="M290 24 C370 8 440 2 500 2 L500 9 C440 9 370 14 290 24Z"/>
    </symbol>
  </defs>
</svg>

<div class="set-label" style="left:858px; top:50px;">Business card</div>
<div class="set-label" style="left:347px; top:814px;">Letterhead</div>
<div class="set-label" style="left:881px; top:814px;">Envelope</div>

<!-- Letterhead -->
<section class="sheet letterhead">
  <div class="brand"><span class="brand-square"></span>HVR LAW</div>
  <div class="contact-line" style="top:24px;"><svg class="contact-icon"><use href="#icon-phone"/></svg>(555) 014-2270</div>
  <div class="contact-line" style="top:38px;"><svg class="contact-icon"><use href="#icon-globe"/></svg>info@yourwebsite.com</div>
  <div class="contact-line" style="top:51px;"><svg class="contact-icon"><use href="#icon-mail"/></svg>www.yourwebsite.com</div>
  <div class="contact-line" style="top:66px; align-items:flex-start;"><svg class="contact-icon" style="height:13px;width:11px;"><use href="#icon-pin"/></svg><span style="text-align:right;line-height:13.5px;">418 Linden Ave. Suite 300<br>Brookfield, TX 75001</span></div>
  <svg class="wave" aria-hidden="true"><use href="#footer-wave" width="100%" height="100%"/></svg>
  <div class="footer-ref">DX-1234 | KWT-00 99 555 777</div>
</section>

<!-- Business card front -->
<section class="sheet card-front">
  <div class="brand brand--white"><span class="brand-square"></span>HVR LAW</div>
  <p class="regulator-note">The Firm is Authorised and Regulated by the KWT</p>
</section>

<!-- Business card back -->
<section class="sheet card-back">
  <div class="brand"><span class="brand-square"></span>HVR LAW</div>
  <div class="person">
    <div class="person-name"><b>Mira</b> Kolar</div>
    <div class="person-role">Founder &amp; CEO</div>
  </div>
  <div class="accent-bar"></div>
  <p class="address">418 Linden Ave. Suite 300<br>Brookfield, TX 75001</p>
  <div class="contact-line" style="top:97px;"><svg class="contact-icon"><use href="#icon-phone"/></svg>(555) 014-2270</div>
  <div class="contact-line" style="top:106px;"><svg class="contact-icon"><use href="#icon-globe"/></svg>info@yourwebsite.com</div>
  <div class="contact-line" style="top:115px;"><svg class="contact-icon"><use href="#icon-mail"/></svg>www.yourwebsite.com</div>
  <svg class="wave" aria-hidden="true"><use href="#footer-wave" width="100%" height="100%"/></svg>
  <div class="footer-ref">DX-1234<br>KWT-00 99 555 777</div>
</section>

<!-- Envelope front -->
<section class="sheet envelope-front">
  <div class="brand"><span class="brand-square"></span>HVR LAW</div>
  <p class="address">418 Linden Ave. Suite 300<br>Brookfield, TX 75001</p>
  <div class="contact-line" style="top:99px;"><svg class="contact-icon"><use href="#icon-phone"/></svg>(555) 014-2270</div>
  <div class="contact-line" style="top:110px;"><svg class="contact-icon"><use href="#icon-mail"/></svg>info@website.com</div>
  <div class="contact-line" style="top:121px;"><svg class="contact-icon"><use href="#icon-globe"/></svg>www.website.com</div>
  <svg class="wave" aria-hidden="true"><use href="#footer-wave" width="100%" height="100%"/></svg>
  <div class="footer-ref">DX-1234 | KWT-00 99 555 777</div>
</section>

<!-- Envelope back -->
<section class="sheet envelope-back">
  <div class="flap"></div>
  <div class="brand brand--white"><span class="brand-square"></span>HVR LAW</div>
</section>

</body>
</html>
```